Plastic Business Card for Bookkeeper

We are looking for a simple professional business card design to use for printing on thin frosted plastic (see-through) card stock. Logo and brand guideline documents are attached as well as a photo of our old business card, and another business card example that we like.

Target Market(s)

Small Business

Industry/Entity Type

Bookkeeper

Contact Information for Business Card

Harriet Olsen CPA
Chief Executive Bookkeeper
T. 03 5926 4417
M. 0438 761 205
E. harriet@pinecrestledger.com
W. www.pinecrestledger.com

Font styles to use
Sans Serif

Colors
6b449b
00a990

Requirements
Must have
• Stick with logo colors. Writing should be clear and easy to read and not too cramped together.
Nice to have
• Tag line for back of the card - 'Clear books, calm business'

```html
<!DOCTYPE html>
<html lang="en">
<head>
<meta charset="utf-8">
<title>Pinecrest Ledger – Business Card</title>
<link rel="stylesheet" href="https://fonts.googleapis.com/css2?family=Montserrat:wght@400;500;700&display=swap">
<style>
  :root {
    --teal: #007b8e;
    --purple: #6b449b;
    --frost-top: #f1eeea;
    --frost-bottom: #e3ded8;
    --white: #ffffff;
    --backdrop: #d8d2ca;
  }
  * { box-sizing: border-box; margin: 0; padding: 0; }
  html, body { width: 1200px; height: 873px; overflow: hidden; }
  body {
    background: var(--backdrop);
    font-family: "Montserrat", sans-serif;
    display: flex;
    flex-direction: column;
    align-items: center;
    justify-content: center;
    gap: 40px;
  }
  .card {
    position: relative;
    width: 580px;
    height: 375px;
    border-radius: 22px;
    overflow: hidden;
    background: linear-gradient(160deg, var(--frost-top), var(--frost-bottom));
    box-shadow: 0 10px 26px rgba(60, 45, 30, 0.22);
  }
  .card-wave { position: absolute; inset: 0; width: 100%; height: 100%; }
  .wordmark {
    position: absolute;
    display: flex;
    align-items: center;
    gap: 14px;
    color: var(--purple);
    font-weight: 700;
    font-size: 30px;
    line-height: 1.05;
    letter-spacing: 0.04em;
  }
  .wordmark-dot {
    width: 26px; height: 26px;
    border-radius: 50%;
    background: var(--teal);
    flex: none;
  }
  .card-front .wordmark { top: 50px; right: 44px; }
  .card-back .wordmark { top: 70px; left: 50%; transform: translateX(-50%); }

  .contact-person {
    position: absolute;
    left: 34px;
    top: 212px;
    color: var(--white);
  }
  .person-name { font-size: 25px; font-weight: 700; line-height: 1.2; }
  .person-role { font-size: 15px; font-weight: 500; margin-top: 2px; }
  .phone-list { list-style: none; margin-top: 12px; font-size: 16px; font-weight: 500; }
  .phone-list li { display: flex; align-items: center; gap: 9px; margin-top: 3px; }
  .phone-icon { width: 15px; height: 15px; fill: var(--white); flex: none; }

  .contact-web {
    position: absolute;
    right: 32px;
    bottom: 22px;
    text-align: right;
    color: var(--white);
    font-size: 17px;
    font-weight: 500;
    line-height: 1.45;
  }
  .tagline {
    position: absolute;
    left: 0; right: 0;
    bottom: 52px;
    text-align: center;
    color: var(--white);
    font-size: 24px;
    font-weight: 700;
  }
</style>
</head>
<body>

  <section class="card card-front" aria-label="Business card front">
    <svg class="card-wave" viewBox="0 0 580 375" preserveAspectRatio="none" aria-hidden="true">
      <path d="M0 128 C 190 118, 370 248, 580 288 L580 375 L0 375 Z" fill="var(--purple)"/>
      <path d="M0 140 C 190 130, 370 260, 580 300 L580 375 L0 375 Z" fill="var(--teal)"/>
    </svg>

    <div class="wordmark">
      <span class="wordmark-dot"></span>
      <span>PINECREST<br>LEDGER</span>
    </div>

    <div class="contact-person">
      <p class="person-name">Harriet Olsen CPA</p>
      <p class="person-role">Chief Executive Bookkeeper</p>
      <ul class="phone-list">
        <li>
          <svg class="phone-icon" viewBox="0 0 24 24" aria-hidden="true">
            <path d="M6.6 10.8a15.1 15.1 0 0 0 6.6 6.6l2.2-2.2a1 1 0 0 1 1-.25 11.4 11.4 0 0 0 3.6.57 1 1 0 0 1 1 1V20a1 1 0 0 1-1 1A17 17 0 0 1 3 4a1 1 0 0 1 1-1h3.5a1 1 0 0 1 1 1c0 1.25.2 2.46.57 3.6a1 1 0 0 1-.25 1z"/>
          </svg>
          03 5926 4417
        </li>
        <li>
          <svg class="phone-icon" viewBox="0 0 24 24" aria-hidden="true">
            <path d="M7 1h10a2 2 0 0 1 2 2v18a2 2 0 0 1-2 2H7a2 2 0 0 1-2-2V3a2 2 0 0 1 2-2zm0 3v14h10V4zm5 15.2a1.2 1.2 0 1 0 0 2.4 1.2 1.2 0 0 0 0-2.4z"/>
          </svg>
          0438 761 205
        </li>
      </ul>
    </div>

    <div class="contact-web">
      <p>harriet@pinecrestledger.com</p>
      <p>www.pinecrestledger.com</p>
    </div>
  </section>

  <section class="card card-back" aria-label="Business card back">
    <svg class="card-wave" viewBox="0 0 580 375" preserveAspectRatio="none" aria-hidden="true">
      <path d="M0 196 C 170 168, 390 258, 580 236 L580 375 L0 375 Z" fill="var(--purple)"/>
      <path d="M0 208 C 170 180, 390 270, 580 248 L580 375 L0 375 Z" fill="var(--teal)"/>
    </svg>

    <div class="wordmark">
      <span class="wordmark-dot"></span>
      <span>PINECREST<br>LEDGER</span>
    </div>

    <p class="tagline">Clear books, calm business</p>
  </section>

</body>
</html>
```